Copperline Business Management Business Card Design Project

I have a new business called Copperline Business Management Limited. We provide business services for the UK for areas which include

Mentoring / Coaching
Interim Management
Non Executive Director / Chairman placement
Angel Investment support
Merger & Acquisition advice
Selling your business advice

I would like a background colour on the logo, a logo and our company name on the logo if possible.

I am open to colours but we want to portray a strong safe business with credibility

The business card design must match that of the logo design
Updates

Target Market(s)

SME and Medium size businesses with the owners, MD's, CEO or senior management as the target audiabce

Industry/Entity Type

Business

Requirements
Must have
• Match the logo design.
Look professional and quality
Should not have
• Old style text and colours
Poor logos depicting money

```html
<!DOCTYPE html>
<html lang="en">
<head>
<meta charset="utf-8">
<title>Copperline Business Management – Business Card</title>
<link href="https://fonts.googleapis.com/css2?family=Questrial&display=swap" rel="stylesheet">
<style>
  :root {
    --backdrop: #2e2f31;
    --card-grey: #bbbcbf;
    --brand-teal: #004f64;
    --arc-sky: #27a6e1;
    --arc-indigo: #3e4fa6;
    --text-light: #e6eef1;
    --text-dark: #262a2e;
    --marker: #3e4fa6;
  }
  html, body {
    margin: 0;
    padding: 0;
    width: 1200px;
    height: 799px;
    overflow: hidden;
    background: var(--backdrop);
  }
  .canvas {
    position: relative;
    width: 1200px;
    height: 799px;
  }
  .business-card {
    position: absolute;
    left: 100px;
    top: 113px;
    width: 1000px;
    height: 572px;
    border-radius: 34px;
    overflow: hidden;
    background: var(--card-grey);
    font-family: "Questrial", "Century Gothic", sans-serif;
  }
  .card-shapes {
    position: absolute;
    inset: 0;
  }
  .company-name {
    position: absolute;
    left: 74px;
    top: 196px;
    margin: 0;
    color: var(--text-light);
    font-weight: 400;
    font-size: 34px;
    line-height: 42px;
    text-align: left;
  }
  .company-name span {
    display: block;
  }
  .tagline {
    position: absolute;
    left: 74px;
    top: 418px;
    margin: 0;
    color: var(--text-light);
    font-size: 22px;
  }
  .service-list {
    position: absolute;
    right: 58px;
    top: 292px;
    margin: 0;
    padding: 0;
    list-style: none;
    text-align: right;
    color: var(--text-dark);
    font-size: 25px;
    line-height: 31px;
  }
  .service-list li::after {
    content: "";
    display: inline-block;
    margin-left: 12px;
    width: 0;
    height: 0;
    border-top: 5px solid transparent;
    border-bottom: 5px solid transparent;
    border-right: 9px solid var(--marker);
    vertical-align: middle;
  }
  .service-list .group-gap {
    margin-top: 18px;
  }
</style>
</head>
<body>
<main class="canvas">
  <section class="business-card" aria-label="Copperline Business Management business card">
    <svg class="card-shapes" width="1000" height="572" viewBox="0 0 1000 572" aria-hidden="true">
      <circle cx="170" cy="250" r="470" fill="var(--arc-indigo)"/>
      <circle cx="170" cy="250" r="459" fill="var(--arc-sky)"/>
      <circle cx="170" cy="250" r="444" fill="var(--brand-teal)"/>
    </svg>

    <h1 class="company-name">
      <span>Copperline</span>
      <span>Business Management Ltd</span>
    </h1>

    <p class="tagline">Selling your business advice</p>

    <ul class="service-list">
      <li>Mentoring / Coaching</li>
      <li>Interim Management</li>
      <li>Non Executive Director</li>
      <li>Chairman placement</li>
      <li class="group-gap">Angel Investment support</li>
      <li>Merger &amp; Acquisition advice</li>
    </ul>
  </section>
</main>
</body>
</html>
```